Media & Printing Company 6 Page Brochure with a Social Justice Theme

We are a printing company that offers most media communication services such as design, web design, mobile app and of course printing. All the profits of the company are used to fund a Social Justice Organisation called “Bright Lantern”. We are looking for a 6 page brochure, flat size 630mm x 210mm fold down to 210mm x 210mm. The brochure needs to push the need for companies to use our service on a “Corporate Social Responsibility” basis with losing the site that we are printers and designers.

Looking for a clean design with impact. A file is attached which shows our logo and some copy to give you an idea of what we are.

Industry/Entity Type

Communication

```html
<!DOCTYPE html>
<html lang="en">
<head>
<meta charset="utf-8">
<title>Loudwave Media Communications – Brochure Cover</title>
<link rel="stylesheet" href="https://fonts.googleapis.com/css2?family=Roboto:ital,wght@1,900&family=Questrial&family=Mulish:ital,wght@1,400&family=Oswald:wght@500&display=swap">
<style>
  :root {
    --stage: #ececec;
    --band-blue: rgba(30, 140, 212, 0.86);
    --band-white: rgba(255, 255, 255, 0.9);
    --ink-white: #ffffff;
    --ink-dark: #2b3340;
    --ink-grey: #4a4a4a;
    --rule: #23303f;
    --logo-grey: #6b6b6b;
    --photo-light: #f3f5f7;
    --photo-steel: #b9c0c6;
    --photo-skin: #d99a86;
    --photo-navy: #2e4466;
  }
  * { box-sizing: border-box; margin: 0; padding: 0; }
  html, body {
    width: 1200px; height: 1001px; overflow: hidden;
    background: var(--stage);
  }
  .cover {
    position: absolute; left: 190px; top: 90px;
    width: 820px; height: 820px; overflow: hidden;
    box-shadow: 0 10px 30px rgba(0,0,0,0.18);
  }
  .cover-photo {
    position: absolute; inset: 0;
    background:
      radial-gradient(ellipse 38% 30% at 38% 22%, var(--photo-steel) 0%, rgba(185,192,198,0) 100%),
      radial-gradient(ellipse 40% 35% at 12% 80%, var(--photo-skin) 0%, rgba(217,154,134,0) 100%),
      radial-gradient(ellipse 30% 22% at 85% 12%, #e7b8a8 0%, rgba(231,184,168,0) 100%),
      radial-gradient(ellipse 45% 45% at 85% 85%, var(--photo-navy) 0%, rgba(46,68,102,0) 100%),
      linear-gradient(160deg, var(--photo-light) 0%, #e4e6e8 55%, #c9a89c 100%);
  }
  .title-band {
    position: absolute; left: 40px; top: 245px;
    width: 540px; height: 210px;
    background: var(--band-blue);
    text-align: center; padding-top: 26px;
  }
  .title-band__name {
    font-family: 'Roboto', sans-serif; font-weight: 900; font-style: italic;
    font-size: 100px; line-height: 1; color: var(--ink-white);
    letter-spacing: 1px;
  }
  .title-band__rule {
    width: 430px; height: 2px; margin: 12px auto 10px;
    background: var(--rule);
  }
  .title-band__sub {
    font-family: 'Questrial', sans-serif; font-size: 31px;
    color: var(--ink-white); letter-spacing: 1px;
  }
  .tagline-band {
    position: absolute; left: 40px; top: 455px;
    width: 540px; height: 100px;
    background: var(--band-white);
    display: flex; align-items: center; justify-content: center;
    text-align: center;
  }
  .tagline-band__text {
    font-family: 'Mulish', sans-serif; font-style: italic; font-size: 22px;
    line-height: 1.25; color: var(--ink-grey);
  }
  .org-mark {
    position: absolute; left: 560px; top: 590px;
    width: 200px; height: 66px;
    background: var(--logo-grey);
    display: flex; align-items: center; gap: 10px; padding: 0 12px;
  }
  .org-mark__square {
    width: 40px; height: 40px; background: var(--ink-white); flex: none;
  }
  .org-mark__name {
    font-family: 'Oswald', sans-serif; font-weight: 500; font-size: 21px;
    line-height: 1.05; color: var(--ink-white); text-transform: uppercase;
  }
</style>
</head>
<body>
  <main class="cover">
    <div class="cover-photo" role="img" aria-label="Photo of a person shouting into a tin-can telephone held up close to the camera"></div>

    <section class="title-band">
      <h1 class="title-band__name">LOUDWAVE</h1>
      <div class="title-band__rule"></div>
      <p class="title-band__sub">MEDIA COMMUNICATIONS</p>
    </section>

    <section class="tagline-band">
      <p class="tagline-band__text">Taking Your Corporate Social<br>Responsibilities To The Next Level</p>
    </section>

    <div class="org-mark">
      <span class="org-mark__square"></span>
      <span class="org-mark__name">Bright<br>Lantern</span>
    </div>
  </main>
</body>
</html>
```